Lantern Image Works

Its a flyer to promote free seminars for alternative photographic techniques. We need to include brief information about the two people who are giving the seminar, Gordon Ashby and Alan Brook and a short description of the methods used. Photo gravure; Gum bichromate, carbon printing. The Seminars are FREE, and will be on march 14th and 15th at Lantern Works Studios, 17 Marlow Road Kingston upon Thames KT4 7QD we would like to add a things saying 'please let us know you are coming on 'lanternimageworks@mailbox.example or via our friendspace page (also called lantern images Works) if we could add a friendspace logo thing
Seminars will be 2 hours long 12 -2 pm

Strap line something like " Discover the creativity of early photographic processes'

And we need the fliers by Saturday!

```html
<!DOCTYPE html>
<html lang="en">
<head>
<meta charset="utf-8">
<title>Lantern Image Works – Free Seminars</title>
<link rel="stylesheet" href="https://fonts.googleapis.com/css2?family=Cinzel:wght@400&family=PT+Sans+Narrow:wght@700&family=Source+Sans+3:wght@400;600;700&display=swap">
<style>
  :root {
    --backdrop: #9b9b9b;
    --flyer-black: #0d0d0d;
    --frame-line: #e8e8e8;
    --text-light: #f4f4f4;
    --accent-red: #a23a29;
    --band-red: #98392a;
    --band-red-dark: #7e2d20;
  }
  * { box-sizing: border-box; margin: 0; padding: 0; }
  html, body { width: 1200px; height: 900px; overflow: hidden; }
  body { background: var(--backdrop); position: relative; font-family: "Source Sans 3", sans-serif; }

  .flyer {
    position: absolute; left: 60px; top: 48px; width: 1080px; height: 762px;
    background:
      radial-gradient(ellipse 38% 70% at 62% 62%, rgba(90,90,90,.55), transparent 70%),
      linear-gradient(180deg, #070707 0%, var(--flyer-black) 40%, #222 100%);
    overflow: hidden;
  }

  .photo-frame { position: absolute; border: 1.5px solid var(--frame-line); border-radius: 14px; padding: 8px; }
  .photo-frame .photo { width: 100%; height: 100%; border-radius: 10px; }
  .frame-portrait { left: 30px; top: 38px; width: 228px; height: 334px; }
  .frame-city { left: 280px; top: 38px; width: 227px; height: 334px; }
  .frame-forest { left: 30px; top: 390px; width: 228px; height: 334px; }
  .frame-dancer { left: 280px; top: 390px; width: 227px; height: 206px; }

  .photo-portrait { background: radial-gradient(ellipse 55% 60% at 48% 40%, #8a8a8a, #3c3c3c 60%, #111 100%); }
  .photo-city { background: linear-gradient(180deg, #8d9a88 0%, #a78a5c 35%, #5a4a3a 70%, #6f5a48 100%); }
  .photo-forest { background: radial-gradient(ellipse 80% 85% at 50% 45%, #b9c9c4 0%, #4f7d8c 40%, #1d3441 75%, #5a3a22 100%); }
  .photo-dancer { background: radial-gradient(ellipse 45% 40% at 50% 50%, #b9a8a6, #5a4442 55%, #2a1c1c 100%); }

  .intro { position: absolute; left: 505px; top: 0; width: 570px; height: 380px; text-align: center; color: var(--text-light); }
  .intro > * { position: absolute; left: 0; width: 100%; white-space: nowrap; }
  .strapline { top: 43px; font-family: "Cinzel", serif; font-weight: 400; font-size: 27px; line-height: 37px; letter-spacing: 1px; }
  .presenters { top: 128px; font-family: "Cinzel", serif; font-weight: 400; font-size: 40px; line-height: 52px; color: var(--accent-red); letter-spacing: 1px; }
  .processes { top: 232px; font-family: "PT Sans Narrow", sans-serif; font-weight: 700; font-size: 25px; line-height: 30px; }
  .processes .dot { margin: 0 4px; }
  .description { top: 278px; font-size: 25px; line-height: 35px; }

  .seminar-box {
    position: absolute; left: 528px; top: 392px; width: 520px; height: 203px;
    border: 1.5px solid var(--frame-line); border-radius: 14px;
    text-align: center; color: var(--text-light); padding-top: 20px; white-space: nowrap;
  }
  .seminar-title { font-family: "Cinzel", serif; font-weight: 400; font-size: 56px; line-height: 60px; letter-spacing: 2px; }
  .seminar-dates { font-size: 25px; line-height: 32px; margin-top: 6px; }
  .seminar-venue { font-size: 25px; line-height: 32px; }
  .seminar-address { font-size: 21px; line-height: 32px; }

  .contact-band {
    position: absolute; left: 280px; top: 624px; width: 800px; height: 90px;
    background: linear-gradient(90deg, var(--band-red-dark), var(--band-red) 40%, var(--band-red));
    border-radius: 12px 0 0 12px; color: var(--text-light);
  }
  .rsvp { position: absolute; left: 14px; top: 18px; width: 490px; text-align: center; white-space: nowrap; }
  .rsvp-note { font-size: 18px; line-height: 24px; }
  .rsvp-email { font-size: 21px; line-height: 32px; margin-top: 2px; }
  .social { position: absolute; left: 532px; top: 18px; display: flex; align-items: center; gap: 20px; }
  .social-square { width: 54px; height: 54px; background: var(--text-light); flex: none; }
  .social-text { font-weight: 700; color: var(--text-light); line-height: 1; white-space: nowrap; }
  .social-lead { font-size: 21px; }
  .social-name { font-size: 31px; margin-top: 3px; }
</style>
</head>
<body>
  <main class="flyer">
    <div class="photo-frame frame-portrait"><div class="photo photo-portrait" role="img" aria-label="Black and white portrait photograph"></div></div>
    <div class="photo-frame frame-city"><div class="photo photo-city" role="img" aria-label="Gum bichromate print of a misty waterside town at dusk"></div></div>
    <div class="photo-frame frame-forest"><div class="photo photo-forest" role="img" aria-label="Blue toned print of bare trees reflected in water"></div></div>
    <div class="photo-frame frame-dancer"><div class="photo photo-dancer" role="img" aria-label="Sepia print of a leaping dancer"></div></div>

    <section class="intro">
      <h2 class="strapline">Discover the creativity of<br>early photographic processes</h2>
      <h1 class="presenters">Gordon Ashby<br>and Alan Brook</h1>
      <p class="processes">Photo Gravure <span class="dot">•</span> Gum Bichromate <span class="dot">•</span> Carbon Printing</p>
      <p class="description">Experience the creativity of traditional<br>photographic and printing techniques.</p>
    </section>

    <section class="seminar-box">
      <h2 class="seminar-title">FREE Seminars</h2>
      <p class="seminar-dates">March 14th and 15th</p>
      <p class="seminar-venue">@ Lantern Works Studios</p>
      <p class="seminar-address">17 Marlow Road Kingston upon Thames KT4 7QD</p>
    </section>

    <footer class="contact-band">
      <div class="rsvp">
        <p class="rsvp-note">Please let us know you are coming on!</p>
        <p class="rsvp-email">email us: lanternimageworks@mailbox.example</p>
      </div>
      <div class="social">
        <div class="social-square" aria-hidden="true"></div>
        <div class="social-text">
          <p class="social-lead">Find us on</p>
          <p class="social-name">friendspace</p>
        </div>
      </div>
    </footer>
  </main>
</body>
</html>
```